Stylish new business card needed!

Hello everyone! I am in need of a new business card design for an alarm company here in Hurricane WV. I have all fonts, color codes and logos provided for you use! We are a young company and like the style of a clean sleek looking business card. Would like it double sided, one side holding the logo and the other with your design!
Target Market(s)
The people that are looking for the newest tech for home automation and security
Industry/Entity Type
Alarm services; Home automation
Contact Information for Business Card
Name of person; position (Sales; Installer); Phone Number (555.419.7362); Employee cell Number; Website (www.GuardedByVelm.example); Employee Email; Double sided
Look and feel
Each slider illustrates characteristics of the customer's brand and the style your logo design should communicate.

```html
<!DOCTYPE html>
<html lang="en">
<head>
<meta charset="utf-8">
<title>Velm Business Card</title>
<link href="https://fonts.googleapis.com/css2?family=Montserrat:wght@400;700&display=swap" rel="stylesheet">
<style>
  :root {
    --backdrop: #dcdddf;
    --paper: #f0efed;
    --edge: #f0843a;
    --grey: #8f8f8f;
    --text-grey: #6b6b6b;
    --orange: #f0843a;
    --rule: #d2d1ce;
  }
  html, body {
    margin: 0;
    width: 1200px;
    height: 1051px;
    overflow: hidden;
    background: var(--backdrop);
    font-family: "Montserrat", Arial, sans-serif;
  }
  .sheet {
    width: 1200px;
    height: 1051px;
    display: flex;
    flex-direction: column;
    align-items: center;
    justify-content: center;
    gap: 70px;
  }
  .card {
    position: relative;
    width: 700px;
    height: 400px;
    background: var(--paper);
    border-bottom: 6px solid var(--edge);
    box-sizing: border-box;
    box-shadow: 0 14px 30px rgba(0,0,0,0.12);
  }
  .wordmark {
    position: absolute;
    display: flex;
    align-items: center;
    gap: 14px;
    color: var(--grey);
    font-weight: 400;
    letter-spacing: 6px;
    line-height: 1;
  }
  .wordmark .dot {
    width: 22px;
    height: 22px;
    border-radius: 50%;
    background: var(--orange);
  }
  .card-front .wordmark {
    top: 70px;
    left: 50%;
    transform: translateX(-50%);
    font-size: 92px;
  }
  .card-back .wordmark {
    top: 50%;
    left: 50%;
    transform: translate(-50%, -50%);
    font-size: 120px;
  }
  .identity {
    position: absolute;
    left: 40px;
    top: 250px;
    width: 250px;
    text-align: right;
  }
  .identity .name {
    color: var(--orange);
    font-weight: 700;
    font-size: 22px;
    letter-spacing: 0.5px;
    margin: 0;
  }
  .identity .role {
    color: var(--text-grey);
    font-size: 16px;
    margin: 6px 0 0;
  }
  .divider {
    position: absolute;
    left: 318px;
    top: 240px;
    width: 1px;
    height: 120px;
    background: var(--rule);
  }
  .contacts {
    position: absolute;
    left: 342px;
    top: 240px;
    margin: 0;
    padding: 0;
    list-style: none;
    color: var(--text-grey);
    font-size: 16px;
  }
  .contacts li {
    display: flex;
    align-items: center;
    gap: 10px;
    height: 30px;
  }
  .contacts svg {
    width: 14px;
    height: 14px;
    fill: var(--orange);
    flex: none;
  }
</style>
</head>
<body>
<main class="sheet">
  <section class="card card-front">
    <div class="wordmark"><span>VELM</span><span class="dot"></span></div>
    <div class="identity">
      <p class="name">OWEN CARRICK</p>
      <p class="role">Installer</p>
    </div>
    <div class="divider"></div>
    <ul class="contacts">
      <li>
        <svg viewBox="0 0 16 16" aria-hidden="true"><path d="M3.5 1l2.5 3-1.5 1.8c.8 1.9 2.2 3.3 4 4.2l1.7-1.6 3.3 2.4-1.2 2.7C7 13.5 2.5 9 1 2.3z"/></svg>
        <span>555.419.7362</span>
      </li>
      <li>
        <svg viewBox="0 0 16 16" aria-hidden="true"><path d="M4.5 0h7A1.5 1.5 0 0 1 13 1.5v13a1.5 1.5 0 0 1-1.5 1.5h-7A1.5 1.5 0 0 1 3 14.5v-13A1.5 1.5 0 0 1 4.5 0zM5 2v10h6V2zm3 11a1 1 0 1 0 0 2 1 1 0 0 0 0-2z"/></svg>
        <span>555.419.7362</span>
      </li>
      <li>
        <svg viewBox="0 0 16 16" aria-hidden="true"><path d="M0 3h16v1.2L8 9 0 4.2zM0 6l8 4.8L16 6v7H0z"/></svg>
        <span>owen@GuardedByVelm.example</span>
      </li>
      <li>
        <svg viewBox="0 0 16 16" aria-hidden="true"><circle cx="8" cy="8" r="7.5"/></svg>
        <span>www.GuardedByVelm.example</span>
      </li>
    </ul>
  </section>

  <section class="card card-back">
    <div class="wordmark"><span>VELM</span><span class="dot"></span></div>
  </section>
</main>
</body>
</html>
```